Quarnel - Business Card Design

Design a modern masculine business card for our business

Target Market(s)

Private Market

Industry/Entity Type

Construction

Contact Information for Business Card

Company Name - Name of Person - Address - email address - contact number

Font styles to use
Serif
Sans Serif

Colors
0094D4
00A9DD
6FCCEA
C7EBF8
E9F6FB
00AB8E
00BBA5
67D7C9
C6EFE9
E9F9F6
F0912C
F2A743
F7CA91
FBE8D2
FDF5EE

Requirements
Must have
• Use company logo provided
Nice to have
• Company Logo

```html
<!DOCTYPE html>
<html lang="en">
<head>
<meta charset="utf-8">
<title>Quarnel Business Card</title>
<link href="https://fonts.googleapis.com/css2?family=Roboto:wght@400;700;900&display=swap" rel="stylesheet">
<style>
  :root{
    --stage:#3c3c3c;
    --paper:#f9f9f9;
    --ink:#161616;
    --accent:#e8621c;
    --back:#202020;
    --back-mark:#2f2f2f;
    --rule:#2a2a2a;
  }
  *{margin:0;padding:0;box-sizing:border-box}
  html,body{width:1200px;height:803px;overflow:hidden}
  body{background:var(--stage);font-family:"Roboto",Arial,sans-serif;color:var(--ink);position:relative}
  .card{position:absolute;top:252px;width:520px;height:298px;border-bottom:3px solid var(--accent);box-shadow:0 18px 40px rgba(0,0,0,.35)}
  .card--front{left:50px;background:var(--paper)}
  .card--back{left:630px;background:var(--back);display:flex;align-items:center;justify-content:center}
  .brand{position:absolute;top:52px;right:40px;display:flex;align-items:center;gap:10px}
  .brand__square{width:22px;height:22px;background:var(--accent)}
  .brand__name{font-weight:900;font-size:44px;letter-spacing:1px;color:var(--ink);line-height:1}
  .person{position:absolute;left:32px;top:132px}
  .person__name{color:var(--accent);font-weight:700;font-size:23px;line-height:1.1}
  .person__title{font-size:13px;margin-top:4px}
  .divider{position:absolute;left:32px;right:40px;top:190px;height:1px;background:var(--rule)}
  .contacts{position:absolute;left:32px;top:202px;list-style:none;font-size:13px;line-height:20px}
  .contacts li{display:flex;align-items:center;gap:10px}
  .contacts svg{width:12px;height:12px;flex:none}
  .address{position:absolute;right:40px;top:202px;font-size:13px;line-height:20px;font-style:normal;text-align:right}
  .back-brand{font-weight:900;font-size:84px;letter-spacing:3px;color:var(--back-mark);line-height:1}
</style>
</head>
<body>
  <section class="card card--front">
    <div class="brand">
      <span class="brand__square"></span>
      <span class="brand__name">QUARNEL</span>
    </div>
    <div class="person">
      <p class="person__name">Daniel Morgan</p>
      <p class="person__title">Managing Director</p>
    </div>
    <div class="divider"></div>
    <ul class="contacts">
      <li><svg viewBox="0 0 12 12"><path d="M2.5 1 L4.5 1 L5 3.5 L3.8 4.5 Q5 7 7.5 8.2 L8.5 7 L11 7.5 L11 9.5 Q10.5 11 9 11 Q1 10 1 3 Q1 1.5 2.5 1Z" fill="var(--accent)"/></svg>555-210-4837</li>
      <li><svg viewBox="0 0 12 12"><rect x="3" y="1" width="6" height="10" rx="1" fill="none" stroke="var(--ink)" stroke-width="1.2"/></svg>555-318-6420</li>
      <li><svg viewBox="0 0 12 12"><rect x="1" y="2.5" width="10" height="7" fill="var(--accent)"/><path d="M1 2.5 L6 6.5 L11 2.5" fill="none" stroke="#fff" stroke-width="1"/></svg>info@quarnelbuild.com</li>
    </ul>
    <address class="address">
      1420 Birchwood Drive<br>
      Fairbanks, Alaska 99701<br>
      www.quarnelbuild.com
    </address>
  </section>
  <section class="card card--back">
    <span class="back-brand">QUARNEL</span>
  </section>
</body>
</html>
```